Infographics about Plumline Census

Hello, we are NexoraFlux, a leading Big Data and Data Science consultancy firm from The Netherlands. We are looking for an awesome infographic.

Introduction
In order to create a better understanding of the status of Big Data in our little country, together with the biggest Big Data trade show Quarry Summit Fair, we created the Plumline Census. This first national research on Big Data aims at providing insight in use of Big Data. The survey is built on five corner stones: Organization, Data, Technology, Skills and Process.

Design
We are looking for an insightful representation of the key-results of the survey, based on the five corner stones. It may also very well be multiple infographics in order to decrease the information density, but I'll leave that to you.

We are looking for a fresh, funky and attractive design, that is easily understood. Please use the colors (orange and blue) of the survey report. For more information see: http://www.nexoraflux.example/static/images/plumlinecensus/plumlinecensus-resultaten-web.pdf

```html
<!DOCTYPE html>
<html lang="en">
<head>
<meta charset="utf-8">
<title>Plumline Census – Organization</title>
<link href="https://fonts.googleapis.com/css2?family=Anton&family=Fjalla+One&family=Oswald:wght@500;600&family=Roboto+Condensed:ital,wght@0,400;1,400&family=Montserrat:wght@800&display=swap" rel="stylesheet">
<style>
  :root {
    --orange: #f7931e;
    --blue: #2f6fb0;
    --navy: #163b5c;
    --grey: #5d5d5d;
    --peach: #fac896;
    --sand: #d0c4b6;
    --white: #ffffff;
    --line: #444444;
  }
  html, body { margin: 0; padding: 0; width: 906px; height: 1200px; overflow: hidden; }
  body { background: var(--sand); }
  .sheet {
    position: relative; width: 1000px; height: 1324px;
    transform: scale(0.906); transform-origin: 0 0;
    background: linear-gradient(180deg, var(--peach) 10%, var(--sand) 100%);
    font-family: "Roboto Condensed", sans-serif;
  }
  .abs { position: absolute; }
  .masthead { left: 0; top: 0; width: 1000px; height: 137px; background: var(--orange); }
  .masthead h1 {
    margin: 0; position: absolute; left: 0; right: 0; top: 4px; text-align: center;
    font-family: "Anton", sans-serif; font-size: 112px; line-height: 128px; letter-spacing: 2px;
    color: var(--orange); -webkit-text-stroke: 4px var(--blue);
    text-shadow: 0 0 0 var(--white), 3px 3px 0 var(--white);
  }
  .source-bar { left: 0; top: 137px; width: 1000px; height: 51px; background: var(--white);
    text-align: center; font-size: 34px; line-height: 51px; color: var(--grey); font-family: "Fjalla One", sans-serif; font-weight: 400; }
  .source-bar b { font-weight: 400; color: #555; }
  .card-shadow { left: 14px; top: 306px; width: 974px; height: 960px; background: var(--navy); }
  .card { left: 20px; top: 298px; width: 960px; height: 960px; background: var(--white); }
  .ribbon { left: 5px; top: 262px; width: 440px; height: 74px; }
  .ribbon span { position: absolute; left: 22px; top: 8px; font-family: "Montserrat", sans-serif; font-weight: 800;
    font-size: 44px; color: var(--white); letter-spacing: 1px; }
  .frame { left: 38px; top: 362px; width: 935px; height: 851px; border: 1.5px solid var(--line); box-sizing: border-box; }
  .rule { background: var(--line); }
  .badge { width: 58px; height: 58px; border-radius: 50%; background: var(--blue); color: var(--white);
    font-family: "Fjalla One", sans-serif; font-size: 34px; text-align: center; line-height: 58px; }
  .heading { font-family: "Fjalla One", sans-serif; color: var(--blue); font-size: 36px; white-space: nowrap; }
  .big { font-family: "Oswald", sans-serif; font-weight: 600; color: var(--orange); line-height: 1; }
  .pct { font-family: "Oswald", sans-serif; font-weight: 500; color: var(--orange); line-height: 1; }
  .copy { font-style: italic; color: var(--grey); font-size: 35px; line-height: 44px; }
  .label-orange { font-family: "Fjalla One", sans-serif; font-style: italic; color: var(--orange); font-size: 30px; line-height: 34px; text-align: center; }
  .factors-box { left: 54px; top: 692px; width: 903px; height: 206px; border: 2px dashed #333; border-radius: 14px; box-sizing: border-box; }
  .note { left: 40px; width: 930px; top: 912px; text-align: right; font-family: "Fjalla One", sans-serif; font-size: 35px; color: #111; }
  .stat-label { font-style: italic; color: var(--grey); font-size: 32px; line-height: 34px; }
</style>
</head>
<body>
<div class="sheet">
  <header class="masthead abs"><h1>PLUMLINE CENSUS</h1></header>
  <div class="source-bar abs"><b>Source:</b> Plumline Census 2015, 186 participants</div>

  <div class="card-shadow abs"></div>
  <div class="card abs"></div>

  <svg class="ribbon abs" viewBox="0 0 440 74" aria-hidden="true">
    <polygon points="0,0 440,0 405,37 440,74 0,74" fill="#2f6fb0"/>
  </svg>
  <div class="ribbon abs"><span>ORGANIZATION</span></div>

  <div class="frame abs"></div>
  <div class="rule abs" style="left:506px;top:362px;width:1.5px;height:270px"></div>
  <div class="rule abs" style="left:38px;top:631px;width:935px;height:1.5px"></div>
  <div class="rule abs" style="left:38px;top:967px;width:935px;height:1.5px"></div>

  <!-- 1 Opportunities -->
  <div class="badge abs" style="left:26px;top:352px">1</div>
  <div class="heading abs" style="left:92px;top:370px">Opportunities of data</div>
  <div class="big abs" style="left:50px;top:430px;font-size:150px">92</div>
  <div class="pct abs" style="left:186px;top:430px;font-size:80px">%</div>
  <div class="copy abs" style="left:200px;top:438px;width:290px;text-align:right">of organizations<br>say that the<br>opportunities of data</div>
  <div class="copy abs" style="left:64px;top:572px">for their organization are big</div>

  <!-- 2 Budget -->
  <div class="badge abs" style="left:924px;top:352px">2</div>
  <div class="heading abs" style="left:780px;top:378px">Budget</div>
  <div class="big abs" style="left:560px;top:430px;font-size:150px">69</div>
  <div class="pct abs" style="left:696px;top:430px;font-size:80px">%</div>
  <div class="copy abs" style="left:700px;top:438px;width:258px;text-align:right">of<br>organizations<br>will increase their</div>
  <div class="copy abs" style="left:574px;top:572px">budget for big data in 2016</div>

  <!-- 3 Success factors -->
  <div class="badge abs" style="left:196px;top:632px">3</div>
  <div class="heading abs" style="left:276px;top:644px">Most important success factors</div>
  <div class="factors-box abs"></div>
  <div class="copy abs" style="left:60px;top:708px;width:405px;text-align:center">The most important factors<br>of a successful<br>implementation of a big data<br>strategy are</div>
  <div class="label-orange abs" style="left:500px;top:726px;width:205px">Company Vision</div>
  <div class="big abs" style="left:526px;top:770px;font-size:118px">28</div>
  <div class="pct abs" style="left:640px;top:770px;font-size:64px">%</div>
  <div class="label-orange abs" style="left:730px;top:704px;width:220px">Support from<br>the management</div>
  <div class="big abs" style="left:776px;top:770px;font-size:118px">19</div>
  <div class="pct abs" style="left:880px;top:770px;font-size:64px">%</div>
  <div class="note abs" style="width:903px">These factors are more important than Budget, Training, Talent</div>

  <!-- 4 Strategy -->
  <div class="badge abs" style="left:88px;top:996px">4</div>
  <div class="heading abs" style="left:158px;top:1004px">Is Big Data part of your organization strategy?</div>

  <div class="big abs" style="left:58px;top:1068px;font-size:120px">37</div>
  <div class="pct abs" style="left:160px;top:1068px;font-size:56px">%</div>
  <div class="stat-label abs" style="left:148px;top:1148px">Agree</div>

  <div class="big abs" style="left:266px;top:1068px;font-size:120px">27</div>
  <div class="pct abs" style="left:370px;top:1068px;font-size:56px">%</div>
  <div class="stat-label abs" style="left:366px;top:1116px">Partially<br>Agree</div>

  <div class="big abs" style="left:494px;top:1068px;font-size:120px">11</div>
  <div class="pct abs" style="left:594px;top:1068px;font-size:56px">%</div>
  <div class="stat-label abs" style="left:592px;top:1116px">Partially<br>Disagrees</div>

  <div class="big abs" style="left:730px;top:1068px;font-size:120px">12</div>
  <div class="pct abs" style="left:832px;top:1068px;font-size:56px">%</div>
  <div class="stat-label abs" style="left:836px;top:1116px">Totally<br>Disagrees</div>
</div>
</body>
</html>
```